New Website Design for PALVO.org

We are looking for a new website design for PALVO.org. PALVO is a non profit home inspector association based in California. Home Inspectors are people that come out and look at a house before it's purchased to let the buyer know of any defects that may exist.
Our site is based on Joomla so if you'll be able to make a Joomla 3 template as well, please let us know (not required, but a bonus).
We would like to see designs that incorporate royal blue, white and chrome into the site as that's our main business colors.
We would like a place for rotating banners though they don't need to be the same size as the current site.
We would like navigation to be easier to manage with menus only across the top (via drop down menus) where we are going to sort out the items currently on the side. Possibly the front page could have a graphic link to separate portals for Realtors, Home Buyers and Inspectors, but that's just one option.
We would like a good mobile design or something that will scale easily to mobile.
The Find an Inspector feature is important and should stand out. The ZIM PALVOr site
Current home page feels a bit busy. Would like to simplify a bit.

```html
<!DOCTYPE html>
<html lang="en">
<head>
<meta charset="utf-8">
<title>PALVO — Home Inspector Association</title>
<link rel="stylesheet" href="https://fonts.googleapis.com/css2?family=PT+Sans:wght@400;700&family=Open+Sans:wght@400;600;700&display=swap">
<style>
:root{
  --royal:#23389a;
  --royal-dark:#1b2d80;
  --ink:#3a3a3a;
  --muted:#8b8b8b;
  --paper:#f4f4f4;
  --panel:#eaeaea;
  --white:#ffffff;
  --chrome:#c9ccd2;
  --footer:#3d3d3d;
  --footer-base:#2b2b2b;
}
*{box-sizing:border-box;margin:0;padding:0}
html,body{width:1200px;height:2633px;overflow:hidden}
body{position:relative;background:var(--paper);font-family:"Open Sans",Arial,sans-serif;color:var(--ink);font-size:12px}
.abs{position:absolute}
h2,h3,h4{font-family:"PT Sans",Arial,sans-serif}

/* top bar */
.topbar{left:0;top:0;width:1200px;height:53px;background:var(--royal);color:#dfe4f5;font-size:12px}
.topbar .item{position:absolute;top:18px;display:flex;align-items:center;gap:8px}
.topbar .login{position:absolute;right:0;top:0;width:180px;height:53px;background:#e4e4e4;color:#333;font-weight:700;font-size:12px;display:flex;align-items:center;justify-content:center;letter-spacing:.5px}

/* header */
.header{left:0;top:53px;width:1200px;height:127px;background:var(--white)}
.brand{position:absolute;left:182px;top:14px;display:flex;align-items:center;gap:10px}
.brand-dot{width:96px;height:96px;border-radius:50%;background:var(--royal);display:flex;align-items:center;justify-content:center;color:#fff;font-family:"PT Sans",sans-serif;font-weight:700;font-size:22px}
.nav{position:absolute;top:68px;left:393px;display:flex;gap:34px;font-family:"PT Sans",sans-serif;font-weight:700;font-size:15px;color:#333}
.nav .active{color:var(--royal)}
.search{position:absolute;left:988px;top:60px;width:28px;height:28px;border:1px solid #ccc;border-radius:50%}

/* hero */
.hero{left:0;top:180px;width:1200px;height:408px;background:linear-gradient(135deg,#3d5d8a 0%,#8fb3d6 35%,#d7e6f2 55%,#4a6d99 80%,#1e3357 100%)}
.hero-panel{left:608px;top:180px;width:412px;height:355px;background:rgba(28,28,32,.86);color:#fff;text-align:center}
.hero-panel h2{margin-top:62px;font-size:24px;line-height:34px;letter-spacing:.5px}
.hero-panel p{margin:22px auto 0;width:320px;font-size:14px;line-height:20px;color:#e6e6e6}
.hero-panel .more{margin-top:50px;display:flex;justify-content:center;align-items:center;gap:10px;font-size:12px;color:#ddd}

.circle-btn{width:18px;height:18px;border-radius:50%;background:#444;display:inline-flex;align-items:center;justify-content:center}
.circle-btn.light{background:#fff}

/* features */
.feature{top:655px;width:300px;text-align:center}
.feature .icon{width:100px;height:100px;border-radius:50%;background:#e1e1e1;margin:0 auto;display:flex;align-items:center;justify-content:center}
.feature .icon span{width:80px;height:80px;border-radius:50%;background:var(--royal);display:flex;align-items:center;justify-content:center}
.feature h3{margin-top:32px;font-size:18px;color:#333}
.feature p{margin:14px auto 0;width:210px;font-size:10.5px;line-height:15px;color:var(--muted)}

/* about band */
.about-band{left:0;top:906px;width:1200px;height:801px;background:var(--panel)}
.section-title{font-size:15px;font-weight:700;color:#333}
.photo{background:linear-gradient(135deg,#c8ced6,#eef1f4 50%,#9aa5b3)}
.welcome h4{font-size:13px;line-height:20px;color:var(--royal)}
.welcome p{margin-top:8px;font-size:10.5px;line-height:15px;color:var(--muted)}
.link-more{display:flex;align-items:center;gap:12px;font-size:10.5px;color:var(--muted)}

.press-banner{left:180px;top:1130px;width:840px;height:83px;background:#fff;box-shadow:0 2px 4px rgba(0,0,0,.08)}
.press-banner h4{position:absolute;left:38px;top:22px;font-size:13px;color:#333}
.press-banner p{position:absolute;left:38px;top:48px;font-size:10.5px;color:#666}
.press-banner p b{color:var(--royal);font-weight:400}
.press-banner .cta{position:absolute;right:0;top:0;width:173px;height:83px;background:var(--royal);color:#fff;font-family:"PT Sans",sans-serif;font-weight:700;font-size:16px;display:flex;align-items:center;justify-content:center}
.press-banner .cta::before{content:"";position:absolute;left:-14px;top:28px;border:14px solid transparent;border-right-color:var(--royal);border-left:0}

.caption{font-size:10.5px;line-height:15px;color:var(--muted);text-align:center}
.why-title{left:0;width:1200px;top:1480px;text-align:center;color:var(--royal);font-size:16px;font-weight:700}
.why-item{width:210px;display:flex;gap:10px}
.why-item .ic{flex:none;width:24px;height:24px;border-radius:50%;background:var(--royal);display:flex;align-items:center;justify-content:center}
.why-item h4{font-size:13px;color:var(--royal-dark)}
.why-item p{margin-top:4px;font-size:10px;line-height:15px;color:#666;white-space:nowrap}

/* info columns */
.col-title{font-size:13px;font-weight:700;color:#333}
.event{display:flex;gap:16px}
.event .date{flex:none;width:42px;height:42px;background:var(--royal);color:#fff;text-align:center;font-family:"PT Sans",sans-serif;font-weight:700;font-size:14px;padding-top:6px;line-height:14px}
.event .date small{display:block;font-size:8px;font-weight:400}
.event .date.grey{background:#9a9a9a}
.event h5{font-size:11px;color:var(--royal)}
.event .meta{font-size:9px;color:var(--muted);margin:3px 0 6px}
.event p{font-size:10.5px;line-height:15px;color:#888}
.acc{display:flex;align-items:center;gap:14px;font-size:10.5px;color:#666;height:38px}
.acc .box{flex:none;width:18px;height:18px;background:#ddd;color:#666;display:flex;align-items:center;justify-content:center;font-weight:700;font-size:13px}
.acc .box.open{background:var(--royal);color:#fff}
.quote{left:761px;top:1790px;width:258px;height:92px;background:var(--royal);color:#fff;font-size:10.5px;line-height:15px;padding:16px 14px}
.quote::after{content:"";position:absolute;right:16px;bottom:-12px;border:12px solid transparent;border-top-color:var(--royal);border-right:0}

/* partners */
.partners-title{left:180px;top:2110px;font-size:15px;font-weight:700;color:var(--royal)}
.partner{top:2160px;height:70px;display:flex;align-items:center;gap:10px;font-family:"PT Sans",sans-serif;font-weight:700;font-size:24px;color:#555}
.partner i{width:20px;height:20px;background:#777;display:block}

/* footer */
.footer{left:0;top:2299px;width:1200px;height:242px;background:var(--footer);color:#ddd}
.footer h4{font-size:13px;color:#fff;margin-bottom:16px}
.footer p{font-size:11px;line-height:16px;color:#d5d5d5}
.thumb{width:76px;height:46px;background:linear-gradient(135deg,#8a96a6,#d2d8de)}
.tweet{width:240px;height:40px;background:#fff;margin-bottom:10px;display:flex;align-items:center;padding:0 8px;gap:10px;font-size:9px;color:#777}
.tweet .dot{flex:none;width:12px;height:12px;border-radius:50%;background:#555}
.tweet .count{margin-left:auto;border-left:1px solid #ddd;padding-left:10px;text-align:center;color:#333;font-size:13px;font-weight:700;line-height:12px}
.tweet .count small{display:block;font-size:7px;font-weight:400;color:#999}
.base{left:0;top:2541px;width:1200px;height:92px;background:var(--footer-base);color:#ccc;font-size:11px}
.base .links{position:absolute;left:420px;top:38px;display:flex;gap:22px}
</style>
</head>
<body>

<div class="abs topbar">
  <div class="item" style="left:180px">
    <svg width="14" height="14" viewBox="0 0 24 24"><path fill="#fff" d="M6.6 10.8a15 15 0 006.6 6.6l2.2-2.2a1 1 0 011-.25 11 11 0 003.6.6 1 1 0 011 1V20a1 1 0 01-1 1A17 17 0 013 4a1 1 0 011-1h3.5a1 1 0 011 1 11 11 0 00.6 3.6 1 1 0 01-.25 1z"/></svg>
    +800 555 0142 or 916 555 0187</div>
  <div class="item" style="left:435px">
    <svg width="16" height="12" viewBox="0 0 16 12"><rect x="0.5" y="0.5" width="15" height="11" rx="1" fill="none" stroke="#fff"/><path d="M1 1l7 6 7-6" fill="none" stroke="#fff"/></svg>
    ceo@palvo.org</div>
  <div class="item" style="left:610px">
    <svg width="14" height="14" viewBox="0 0 14 14"><circle cx="7" cy="7" r="6" fill="none" stroke="#fff"/><circle cx="7" cy="7" r="2" fill="#fff"/></svg>
    ask to PALVO</div>
  <div class="login">LOGIN</div>
</div>

<header class="abs header">
  <div class="brand"><div class="brand-dot">PALVO</div></div>
  <nav class="nav">
    <span class="active">HOME</span><span>ABOUT US</span><span>PRODUCTS</span><span>INFO</span><span>APPLICATIONS</span><span>CONTACT US</span>
  </nav>
  <div class="search"></div>
</header>

<div class="abs hero" role="img" aria-label="Banner photo of a glass and steel building roof seen from below"></div>
<div class="abs hero-panel">
  <h2>LOREM IPSUM DOLAR SIT<br>OMNIS EXPLICABO</h2>
  <p>aspernatur magni quae aperiam averitatis voluptas doloremque error natus natus, qui aut eaque inventore</p>
  <div class="more">amet rem eos <span class="circle-btn light"><svg width="8" height="8" viewBox="0 0 8 8"><path d="M2 1l4 3-4 3z" fill="#222"/></svg></span></div>
</div>

<div class="abs feature" style="left:172px">
  <div class="icon"><span><svg width="30" height="34" viewBox="0 0 30 34"><path d="M4 4h22v14c0 7-5 11-11 13C9 29 4 25 4 18z" fill="#fff"/><path d="M15 8v18" stroke="var(--royal)" stroke-width="3"/></svg></span></div>
  <h3>INSPECTOR FINDER</h3>
  <p>perspiciatis beatae magni architecto odit odit aspernatur magni quae aperiam aut veritatis beatae eos aut voluptas doloremque perspiciatis</p>
</div>
<div class="abs feature" style="left:447px">
  <div class="icon"><span><svg width="36" height="36" viewBox="0 0 36 36"><circle cx="18" cy="18" r="16" fill="#fff"/><rect x="9" y="12" width="18" height="12" fill="var(--royal)"/><path d="M9 12l9 7 9-7" fill="none" stroke="#fff" stroke-width="1.5"/></svg></span></div>
  <h3>TIE MESSAGE BOARDS</h3>
  <p>perspiciatis beatae magni architecto odit odit aspernatur magni quae aperiam aut veritatis beatae eos aut voluptas doloremque perspiciatis</p>
</div>
<div class="abs feature" style="left:725px">
  <div class="icon"><span><svg width="34" height="34" viewBox="0 0 34 34"><path d="M4 16V4h12l15 15-12 12z" fill="#fff"/><circle cx="10" cy="10" r="2.5" fill="var(--royal)"/></svg></span></div>
  <h3>PALVO ONLINE STORE</h3>
  <p>perspiciatis beatae magni architecto odit odit aspernatur magni quae aperiam aut veritatis beatae eos aut voluptas doloremque perspiciatis</p>
</div>

<section class="abs about-band">
  <h2 class="abs section-title" style="left:182px;top:26px">ABOUT US</h2>
  <div class="abs photo" style="left:182px;top:59px;width:191px;height:106px" role="img" aria-label="Photo of colleagues meeting at a laptop"></div>
  <div class="abs photo" style="left:384px;top:59px;width:191px;height:106px" role="img" aria-label="Photo of a businessman at a desk"></div>
  <div class="abs photo" style="left:586px;top:59px;width:191px;height:106px" role="img" aria-label="Photo of a team gathered around a table"></div>
  <div class="abs welcome" style="left:801px;top:62px;width:220px">
    <h4>WELCOME TO PALVO<br>CONSEQUNTUR</h4>
    <p>Voluptatem doloremque perspi beatae ratione dolores unde</p>
    <div class="link-more" style="margin-top:12px">learn more <span class="circle-btn"><svg width="8" height="8" viewBox="0 0 8 8"><path d="M2 1l4 3-4 3z" fill="#fff"/></svg></span></div>
  </div>
</section>

<div class="abs press-banner">
  <h4>SED ENIM ACCUSANTIUM LAUDANTIUM INVENTORE IPSA ISTE SUNT SED SIT IPSAM</h4>
  <p>Sed enim accusantium <b>laudantium Unde quas</b> quae ratione inventore ipsa iste sunt sit ipsam ut voluptatem <b>doloremque</b></p>
  <div class="cta">SEE PALVO PERSS</div>
</div>

<h2 class="abs section-title" style="left:180px;top:1260px;color:var(--royal)">RECENT CUSTOMERS</h2>
<p class="abs" style="left:180px;top:1288px;width:200px;font-size:10.5px;line-height:15px;color:var(--muted)">Dolores ut voluptatem doloremque perspi beatae quia ratione ratione dolores Unde quas ratione inventore ipsa explicabo</p>
<div class="abs link-more" style="left:180px;top:1354px">view more <span class="circle-btn"><svg width="8" height="8" viewBox="0 0 8 8"><path d="M2 1l4 3-4 3z" fill="#fff"/></svg></span></div>
<div class="abs photo" style="left:408px;top:1266px;width:191px;height:123px" role="img" aria-label="Photo of a couple shaking hands with an agent"></div>
<div class="abs photo" style="left:614px;top:1266px;width:196px;height:123px" role="img" aria-label="Photo of a group of customers smiling"></div>
<div class="abs photo" style="left:823px;top:1266px;width:195px;height:123px" role="img" aria-label="Photo of clients reviewing documents"></div>
<p class="abs caption" style="left:408px;top:1405px;width:191px">Nemo rem ipsam quas illo<br>dolores ut voluptatem explicabo</p>
<p class="abs caption" style="left:614px;top:1405px;width:196px">Nemo rem ipsam quas illo<br>dolores ut voluptatem explicabo</p>
<p class="abs caption" style="left:823px;top:1405px;width:195px">Nemo rem ipsam quas illo<br>dolores ut voluptatem explicabo</p>
<div class="abs" style="left:540px;top:1452px;width:120px;height:1px;background:#bbb"></div>

<h2 class="abs why-title">WHY CHOOSE US</h2>
<div class="abs" style="left:180px;top:1520px;width:840px;height:1px;background:#d0d0d0"></div>

<div class="abs why-item" style="left:182px;top:1532px"><span class="ic"><svg width="12" height="12" viewBox="0 0 12 12"><path d="M2 10l6-6 2 2-6 6H2z" fill="#fff"/></svg></span><div><h4>IPSA EXPLICABO</h4><p>Dolores ut voluptatem doloremque<br>beatae ratione ratione dolores</p></div></div>
<div class="abs why-item" style="left:397px;top:1532px"><span class="ic"><svg width="12" height="12" viewBox="0 0 12 12"><path d="M2 6l3 3 5-6" fill="none" stroke="#fff" stroke-width="2"/></svg></span><div><h4>RATIONE INVENTORE</h4><p>Dolores ut voluptatem doloremque<br>beatae ratione ratione dolores</p></div></div>
<div class="abs why-item" style="left:612px;top:1532px"><span class="ic"><svg width="12" height="12" viewBox="0 0 12 12"><path d="M1 2h10v6H5l-3 3V8H1z" fill="#fff"/></svg></span><div><h4>UNDE QUASI</h4><p>Dolores ut voluptatem doloremque<br>beatae ratione ratione dolores</p></div></div>
<div class="abs why-item" style="left:825px;top:1532px"><span class="ic"><svg width="12" height="12" viewBox="0 0 12 12"><rect x="2" y="2" width="8" height="8" fill="none" stroke="#fff" stroke-width="1.5"/><path d="M4 5h4M4 7h4" stroke="#fff"/></svg></span><div><h4>CUSTOMER SUPPORT</h4><p>Dolores ut voluptatem doloremque<br>beatae ratione ratione dolores</p></div></div>

<div class="abs why-item" style="left:182px;top:1608px"><span class="ic"><svg width="12" height="12" viewBox="0 0 12 12"><ellipse cx="6" cy="5" rx="5" ry="3.5" fill="#fff"/><path d="M3 8l-1 3 3-2z" fill="#fff"/></svg></span><div><h4>RATIONE DOLORES</h4><p>Dolores ut voluptatem doloremque<br>beatae ratione ratione dolores</p></div></div>
<div class="abs why-item" style="left:397px;top:1608px"><span class="ic"><svg width="12" height="12" viewBox="0 0 12 12"><rect x="1.5" y="2" width="9" height="7" fill="none" stroke="#fff" stroke-width="1.5"/><path d="M4 11h4" stroke="#fff"/></svg></span><div><h4>BEATAE QUIA</h4><p>Dolores ut voluptatem doloremque<br>beatae ratione ratione dolores</p></div></div>
<div class="abs why-item" style="left:612px;top:1608px"><span class="ic"><svg width="12" height="12" viewBox="0 0 12 12"><circle cx="6" cy="6" r="4" fill="none" stroke="#fff" stroke-width="1.5"/><path d="M6 6V3" stroke="#fff"/></svg></span><div><h4>BEATAE ATIONE</h4><p>Dolores ut voluptatem doloremque<br>beatae ratione ratione dolores</p></div></div>
<div class="abs why-item" style="left:825px;top:1608px"><span class="ic"><svg width="12" height="12" viewBox="0 0 12 12"><path d="M2 3h8M2 6h8M2 9h8" stroke="#fff" stroke-width="1.5"/></svg></span><div><h4>CUSTOMER SUPPORT</h4><p>Dolores ut voluptatem doloremque<br>beatae ratione ratione dolores</p></div></div>

<!-- info columns -->
<h3 class="abs col-title" style="left:180px;top:1765px">UPCOMING EVENTS</h3>
<div class="abs link-more" style="left:358px;top:1764px">view more <span class="circle-btn"><svg width="8" height="8" viewBox="0 0 8 8"><path d="M2 1l4 3-4 3z" fill="#fff"/></svg></span></div>
<div class="abs event" style="left:180px;top:1795px;width:270px">
  <div class="date">10<small>Jan</small></div>
  <div><h5>Veritatis beatae eos aut voluptas</h5><p class="meta">Doloremque Totam | 9 Comments</p>
  <p>Enim accusantium laudantium laudantium perspiciatis ipsam sed doloremque ipsam dolores totam unde unde, et aut illo aut</p></div>
</div>
<div class="abs event" style="left:180px;top:1910px;width:270px">
  <div class="date grey">10<small>Jan</small></div>
  <div><h5 style="color:#555">Perspiciatis error natus aut eaque</h5><p class="meta">Doloremque Totam | 9 Comments</p>
  <p>dolores totam unde unde, et aut illo aut veritatis explicabo dicta quo veritatis</p></div>
</div>

<h3 class="abs col-title" style="left:487px;top:1765px">INSPECTOR NEWS</h3>
<div class="abs" style="left:487px;top:1790px;width:240px">
  <div class="acc"><span class="box open">−</span>Doloremque perspiciatis error</div>
  <p style="font-size:10.5px;line-height:15px;color:#888;margin:10px 0 8px 32px">Enim accusantium laudantium laudantium perspiciatis ipsam sed doloremque ipsam dolores totam unde, et aut illo aut</p>
  <div class="acc"><span class="box">+</span><span style="color:var(--royal)">Fugit aut illo omnis explicabo ipsa</span></div>
  <div class="acc"><span class="box">+</span>Rem ipsam quas illo dolores</div>
  <div class="acc"><span class="box">+</span>Voluptatem doloremque perspiciatis</div>
</div>

<h3 class="abs col-title" style="left:761px;top:1765px">OUR TESTIMONILAS</h3>
<div class="abs quote">" Voluptatem fugit aut illo omnis explicabo ipsa nemo rem ipsam quas illo dolores et voluptatem doloremque perspiciatis beatae magni architecto odit odit</div>
<div class="abs" style="left:760px;top:1908px;width:212px;text-align:right;font-size:10.5px;line-height:15px"><b style="color:#e07b1a">Noah Reed</b><br>Project Manager</div>
<div class="abs" style="left:978px;top:1902px;width:40px;height:40px;background:linear-gradient(135deg,#b9a79a,#e7ddd4)" role="img" aria-label="Portrait photo of the reviewer"></div>

<!-- partners -->
<div class="abs" style="left:0;top:2051px;width:1200px;height:248px;background:#f0f0f0"></div>
<h2 class="abs partners-title">BEST PARTNER</h2>
<div class="abs partner" style="left:182px"><i></i>Norvale</div>
<div class="abs partner" style="left:406px">Kestro</div>
<div class="abs partner" style="left:553px">Lumara</div>
<div class="abs partner" style="left:730px">Oakfield</div>
<div class="abs partner" style="left:910px"><i style="background:#333"></i>Bramble TV</div>

<!-- footer -->
<footer class="abs footer">
  <div class="abs" style="left:180px;top:58px;width:170px">
    <h4>WHO WE ARE</h4>
    <p>Fugit aut illo omnis explicabo ipsa, nemo ipsam quas dolores voluptatem dolo perspiciatis beatae magni architecto odit</p>
    <p style="margin-top:16px;color:#fff">Read More <span class="circle-btn light" style="width:14px;height:14px;vertical-align:middle"></span></p>
  </div>
  <div class="abs" style="left:398px;top:58px;width:170px">
    <h4>ADREESS</h4>
    <p>2400 Elm Row Suite 110<br>Rivermont CA 90000-0000<br>Hours M-F 8:00am-5:00pm<br>Fax: 916 555 0163</p>
    <p style="margin-top:16px;display:flex;gap:10px;align-items:center"><svg width="10" height="14" viewBox="0 0 10 14"><path d="M5 0a5 5 0 015 5c0 4-5 9-5 9S0 9 0 5a5 5 0 015-5z" fill="#fff"/><circle cx="5" cy="5" r="2" fill="#3d3d3d"/></svg>Open in City Map</p>
  </div>
  <div class="abs" style="left:574px;top:58px;width:170px">
    <h4>PALVO PERSS</h4>
    <div style="display:grid;grid-template-columns:76px 76px;gap:10px">
      <div class="thumb" role="img" aria-label="News photo"></div><div class="thumb" role="img" aria-label="News photo"></div>
      <div class="thumb" role="img" aria-label="News photo"></div><div class="thumb" role="img" aria-label="News photo"></div>
    </div>
  </div>
  <div class="abs" style="left:782px;top:58px">
    <h4>TWEETS</h4>
    <div class="tweet"><span class="dot"></span><span>ratione inventore ipsa<br>quas illo</span><span class="count">2<small>days ago</small></span></div>
    <div class="tweet"><span class="dot"></span><span>ratione inventore ipsa<br>quas illo</span><span class="count">2<small>days ago</small></span></div>
  </div>
</footer>
<div class="abs base">
  <span class="abs" style="left:180px;top:38px">© 2013 PALVO. All Rights Reserved.</span>
  <div class="links"><span>about us</span><span>lates news</span><span>popular</span><span>privacy policy</span><span>FAQs</span><span>contact us</span></div>
</div>

</body>
</html>
```